HARBEN VODKA LABELS DESIGN*

we Need a New label for Premium vodka "Harben Vodka" we are attaching design of current bottle and we need to change logo to Harben vodka with completely new design and concept . Please not that current logo is there just for example"

EXACT SIZE AND SHAPE OF LOGO ATTACHED

Logo Text

"harben vodka

```html
<!DOCTYPE html>
<html lang="en">
<head>
<meta charset="utf-8">
<title>Harben Vodka Label</title>
<link rel="stylesheet" href="https://fonts.googleapis.com/css2?family=Cinzel:wght@400;700&display=swap">
<style>
  :root {
    --bg: #e4e4e6;
    --label-white: #ffffff;
    --rim-gold: #f2b315;
    --ink: #1a1a1a;
    --red-deep: #c0161f;
    --red-bright: #ec4a3a;
    --band-red: #e2392f;
    --band-text: #fbe6d8;
    --base-text: #3a3a3c;
  }
  html, body {
    margin: 0;
    padding: 0;
    width: 1200px;
    height: 1200px;
    overflow: hidden;
    background: var(--bg);
  }
  .canvas {
    width: 1200px;
    height: 1200px;
    position: relative;
  }
  .canvas svg {
    display: block;
  }
  .label-body { fill: var(--label-white); }
  .label-rim { fill: none; stroke: var(--rim-gold); stroke-width: 5; }
  .brand-mark-circle { fill: none; stroke: var(--ink); stroke-width: 4; }
  .brand-mark-name {
    font-family: 'Cinzel', serif;
    font-weight: 700;
    font-size: 44px;
    fill: var(--ink);
  }
  .established {
    font-family: 'Cinzel', serif;
    font-weight: 700;
    font-size: 22px;
    fill: var(--ink);
  }
  .product-name {
    font-family: 'Cinzel', serif;
    font-weight: 700;
    font-size: 76px;
    fill: url(#nameGradient);
    letter-spacing: 1px;
  }
  .product-type {
    font-family: 'Cinzel', serif;
    font-weight: 400;
    font-size: 52px;
    fill: var(--ink);
    letter-spacing: 2px;
  }
  .quality-band { fill: var(--band-red); }
  .quality-text {
    font-family: 'Cinzel', serif;
    font-weight: 400;
    font-size: 28px;
    fill: var(--band-text);
    letter-spacing: 1px;
  }
  .base-name {
    font-family: 'Cinzel', serif;
    font-weight: 700;
    font-size: 68px;
    fill: var(--base-text);
    letter-spacing: 3px;
  }
</style>
</head>
<body>
<div class="canvas">
  <svg width="1200" height="1200" viewBox="0 0 1200 1200" xmlns="http://www.w3.org/2000/svg">
    <defs>
      <linearGradient id="nameGradient" x1="0" y1="0" x2="1" y2="0">
        <stop offset="0" stop-color="var(--red-deep)"/>
        <stop offset="0.55" stop-color="var(--red-bright)"/>
        <stop offset="1" stop-color="var(--red-deep)"/>
      </linearGradient>
      <path id="nameArc" d="M 395 528 Q 600 478 805 528"/>
    </defs>

    <g class="oval-label">
      <ellipse class="label-body" cx="600" cy="450" rx="230" ry="400"/>
      <ellipse class="label-rim" cx="600" cy="450" rx="208" ry="376"/>

      <g class="brand-mark">
        <circle class="brand-mark-circle" cx="488" cy="300" r="30"/>
        <text class="brand-mark-name" x="534" y="315">Harben</text>
      </g>

      <text class="established" x="465" y="404" text-anchor="middle">EST</text>
      <text class="established" x="708" y="404" text-anchor="middle">1867</text>

      <text class="product-name" text-anchor="middle">
        <textPath href="#nameArc" startOffset="50%">HARBEN</textPath>
      </text>
      <text class="product-type" x="600" y="590" text-anchor="middle">VODKA</text>
    </g>

    <g class="quality-strip">
      <rect class="quality-band" x="380" y="935" width="440" height="44"/>
      <text class="quality-text" x="600" y="967" text-anchor="middle">EXTRA FINE QUALITY</text>
    </g>

    <text class="base-name" x="600" y="1110" text-anchor="middle">HARBEN</text>
  </svg>
</div>
</body>
</html>
```